Brightpath Orthodontics business card design

Need a business card design that reflects our re-branding (orthodontic office - braces) and a new partnership with a pediatric dental office. We would like to include "for adults and children" on the card as well so adults know they are welcome to get their braces here as well. Office design is modern and would like business card to reflect a modern type look. Here's the text we would like to be included on the card:

Darren Holloway, DDS, MSD
5214 West Maple Avenue, Suite 204
Mansfield, TX 76099
817-555-0143
www.brightpathortho.example
info@brightpathortho.example
Updates

Can we add the following to the existing designs? Darren Holloway, DDS, MSD 5214 West Maple Avenue, Suite 204 Mansfield, TX 76099 817-555-0143

Does anyone have any more vertical designs available? Thanks!

Industry/Entity Type

Dental

```html
<!DOCTYPE html>
<html lang="en">
<head>
<meta charset="utf-8">
<title>Brightpath Orthodontics – Business Card</title>
<link rel="stylesheet" href="https://fonts.googleapis.com/css2?family=Ubuntu:wght@400;500;700&display=swap">
<style>
  :root {
    --backdrop: #e9e6e1;
    --card: #ffffff;
    --ink: #1a1a1a;
    --yellow: #f7e625;
    --blue: #1b75bb;
    --magenta: #ec168c;
    --green: #8cc63f;
    --orange: #f7941d;
    --name-blue: #1f73b7;
  }
  * { box-sizing: border-box; margin: 0; padding: 0; }
  html, body {
    width: 1200px;
    height: 1023px;
    overflow: hidden;
    background: var(--backdrop);
    font-family: "Ubuntu", sans-serif;
    color: var(--ink);
  }
  .canvas {
    width: 1200px;
    height: 1023px;
    display: flex;
    align-items: center;
    justify-content: center;
  }
  .business-card {
    position: relative;
    width: 500px;
    height: 875px;
    background: var(--card);
    box-shadow: 0 10px 30px rgba(0,0,0,0.18);
    overflow: hidden;
  }
  .color-rail {
    position: absolute;
    left: 0;
    top: 0;
    width: 62px;
    height: 875px;
  }
  .card-content {
    position: absolute;
    left: 62px;
    right: 0;
    top: 0;
    bottom: 0;
    text-align: center;
  }
  .brand {
    margin-top: 118px;
    font-weight: 700;
    color: var(--ink);
    line-height: 1.05;
  }
  .brand-name {
    display: block;
    font-size: 52px;
    letter-spacing: 0.5px;
  }
  .brand-kind {
    display: block;
    font-size: 40px;
  }
  .tagline {
    margin-top: 8px;
    font-size: 22px;
    font-weight: 700;
    color: var(--green);
  }
  .doctor {
    margin-top: 92px;
  }
  .doctor-name {
    font-size: 31px;
    font-weight: 400;
    color: var(--name-blue);
    letter-spacing: 0.5px;
  }
  .doctor-credentials {
    margin-top: 6px;
    font-size: 19px;
    font-weight: 500;
  }
  .address {
    margin-top: 66px;
    font-size: 21px;
    font-weight: 500;
    line-height: 1.45;
    font-style: normal;
  }
  .contact-list {
    list-style: none;
    margin-top: 62px;
    display: inline-flex;
    flex-direction: column;
    align-items: flex-start;
    gap: 8px;
    font-size: 21px;
    font-weight: 500;
  }
  .contact-list li {
    display: flex;
    align-items: center;
    gap: 10px;
  }
  .contact-icon {
    width: 24px;
    height: 24px;
    flex: none;
  }
</style>
</head>
<body>
<main class="canvas">
  <article class="business-card">
    <svg class="color-rail" viewBox="0 0 62 875" aria-hidden="true">
      <polygon points="0,0 62,0 62,160 0,175" fill="var(--yellow)"/>
      <polygon points="0,179 62,164 62,330 0,345" fill="var(--blue)"/>
      <polygon points="0,349 62,334 62,500 0,515" fill="var(--magenta)"/>
      <polygon points="0,519 62,504 62,670 0,685" fill="var(--green)"/>
      <polygon points="0,689 62,674 62,875 0,875" fill="var(--orange)"/>
    </svg>

    <div class="card-content">
      <h1 class="brand">
        <span class="brand-name">Brightpath</span>
        <span class="brand-kind">Orthodontics</span>
      </h1>
      <p class="tagline">For Adults and Children</p>

      <section class="doctor">
        <h2 class="doctor-name">Darren Holloway</h2>
        <p class="doctor-credentials">DDS, MSD</p>
      </section>

      <address class="address">
        5214 West Maple Avenue,<br>
        Suite 204 Mansfield,<br>
        TX 76099
      </address>

      <ul class="contact-list">
        <li>
          <svg class="contact-icon" viewBox="0 0 24 24" aria-hidden="true">
            <rect x="6" y="1.5" width="12" height="21" rx="2.5" fill="none" stroke="var(--magenta)" stroke-width="2"/>
            <line x1="10" y1="19" x2="14" y2="19" stroke="var(--magenta)" stroke-width="2"/>
          </svg>
          <span>817-555-0143</span>
        </li>
        <li>
          <svg class="contact-icon" viewBox="0 0 24 24" aria-hidden="true">
            <rect x="1" y="5" width="22" height="14" fill="var(--green)"/>
            <polyline points="1,5 12,13 23,5" fill="none" stroke="#fff" stroke-width="1.6"/>
          </svg>
          <span>info@brightpathortho.example</span>
        </li>
        <li>
          <svg class="contact-icon" viewBox="0 0 24 24" aria-hidden="true">
            <circle cx="12" cy="12" r="10.5" fill="var(--orange)"/>
            <ellipse cx="12" cy="12" rx="4.5" ry="10.5" fill="none" stroke="#fff" stroke-width="1.4"/>
            <line x1="1.5" y1="12" x2="22.5" y2="12" stroke="#fff" stroke-width="1.4"/>
          </svg>
          <span>www.brightpathortho.example</span>
        </li>
      </ul>
    </div>
  </article>
</main>
</body>
</html>
```